Webdesign Metall- und Stahlbau Harkenfeld GmbH
Zielgruppe
Metall- und Stahlbau Harkenfeld GmbH
Zielgruppe: öffentlicher Bereich, Industrie, Gesundheitswesen > deutschlandweit tätig
Aufgabenstellung
keine bewegten Bilder oder Elemente in der Website
klassisches Layout
sehr konservativ

```html
<!DOCTYPE html>
<html lang="de">
<head>
<meta charset="utf-8">
<title>Metall- und Stahlbau Harkenfeld GmbH</title>
<link href="https://fonts.googleapis.com/css2?family=Outfit:wght@300;400;500;600;700&display=swap" rel="stylesheet">
<style>
:root{
  --navy:#06067a;
  --navy-deep:#04046a;
  --yellow:#f2cb6b;
  --ink:#151515;
  --muted:#555;
  --page:#f5f5f5;
  --white:#fff;
  --line:#dcdcdc;
}
*{box-sizing:border-box;margin:0;padding:0}
html,body{width:778px;height:1200px;overflow:hidden}
body{font-family:"Outfit",sans-serif;background:var(--page);color:var(--ink);position:relative}
.abs{position:absolute}
/* header */
.site-header{position:absolute;left:0;top:0;width:778px;height:51px;background:var(--white)}
.brand{position:absolute;left:123px;top:11px;display:flex;align-items:center;gap:8px}
.brand-mark{width:29px;height:29px;background:var(--navy)}
.brand-text{color:var(--navy);line-height:1.25}
.brand-text .l1{font-size:7px;font-weight:400}
.brand-text .l2{font-size:7.4px;font-weight:600}
.brand-text .l3{font-size:5.4px;font-weight:400}
.meta-nav{position:absolute;right:124px;top:11px;display:flex;gap:12px;font-size:5.2px;color:#333}
.meta-line{position:absolute;left:447px;top:27px;width:208px;height:1px;background:#ececec}
.main-nav{position:absolute;right:123px;top:34px;display:flex;gap:18px;font-size:6.6px;font-weight:500}
.main-nav a{color:var(--ink);text-decoration:none}
.main-nav a.active{color:var(--navy);border-bottom:1.5px solid var(--yellow);padding-bottom:1px}
/* hero */
.hero{position:absolute;left:0;top:51px;width:778px;height:266px}
.hero-panel{position:absolute;left:0;top:0;width:389px;height:266px;background:var(--navy)}
.hero-photo{position:absolute;left:389px;top:0;width:389px;height:266px;background:linear-gradient(135deg,#4c5e76 0%,#2d3a4d 45%,#8a5a40 62%,#3a4658 100%)}
.hero h1{position:absolute;left:123px;top:68px;color:var(--white);font-size:17px;font-weight:600;line-height:1.12}
.hero p{position:absolute;left:123px;top:121px;width:240px;color:var(--white);font-size:7.1px;font-weight:300;line-height:1.6}
.btn{display:inline-flex;align-items:center;justify-content:center;height:19px;border-radius:4px;font-size:7px;font-weight:500;color:var(--navy);text-decoration:none}
.btn-yellow{background:var(--yellow)}
.btn-white{background:var(--white)}
.hero .btn{position:absolute;top:175px}
/* teaser grid */
.photo{position:absolute}
.card{position:absolute;background:var(--white)}
.card .kicker{position:absolute;font-size:7px;font-weight:600;color:var(--navy)}
.card h2{position:absolute;font-size:10.8px;font-weight:600;line-height:1.3}
.card p{position:absolute;font-size:6.7px;font-weight:300;line-height:1.45;color:#333}
.card .btn{position:absolute}
.divider{position:absolute;left:123px;top:667px;width:532px;height:1px;background:var(--line)}
/* tiles */
.tile{position:absolute;top:689px;width:130px;height:126px;background:var(--white);text-align:center}
.tile-icon{position:absolute;left:45px;top:19px;width:40px;height:33px;border-radius:3px;background:var(--navy);display:flex;align-items:center;justify-content:center}
.tile h3{position:absolute;left:0;right:0;top:62px;font-size:8.6px;font-weight:600;color:var(--navy)}
.tile p{position:absolute;left:14px;right:14px;top:78px;font-size:6.4px;font-weight:300;line-height:1.5;color:#222}
.tile-arrow{position:absolute;right:11px;bottom:9px}
/* contact */
.contact-photo{position:absolute;left:0;top:850px;width:387px;height:290px;background:linear-gradient(120deg,#2c3023 0%,#5a5a3e 40%,#6e6352 65%,#3b3a30 100%)}
.contact-panel{position:absolute;left:387px;top:850px;width:391px;height:290px;background:var(--navy)}
.contact-panel h2{position:absolute;left:32px;top:42px;font-size:16px;font-weight:600;color:var(--white)}
.contact-panel h4{position:absolute;left:32px;top:76px;font-size:7.8px;font-weight:500;color:var(--white)}
.info{position:absolute;left:32px;display:flex;gap:4px;color:var(--white);font-size:6.8px;font-weight:300;line-height:1.65}
.info svg{flex:none;margin-top:1.5px}
/* footer */
.site-footer{position:absolute;left:0;top:1140px;width:778px;height:60px;background:var(--page)}
.copyright{position:absolute;left:122px;top:25px;font-size:6.3px;font-weight:300;color:#666}
.legal{position:absolute;right:127px;top:25px;display:flex;gap:14px;font-size:6.8px}
.legal a{color:var(--navy);text-decoration:underline}
</style>
</head>
<body>

<header class="site-header">
  <div class="brand">
    <div class="brand-mark"></div>
    <div class="brand-text">
      <div class="l1">Metall- und Stahlbau</div>
      <div class="l2">HARKENFELD GMBH</div>
      <div class="l3">Meisterbetrieb der Innung seit 1965</div>
    </div>
  </div>
  <nav class="meta-nav"><span>News</span><span>Karriere</span><span>Downloads</span></nav>
  <div class="meta-line"></div>
  <nav class="main-nav">
    <a class="active" href="#">Home</a><a href="#">Leistungen</a><a href="#">Referenzen</a><a href="#">Über uns</a><a href="#">Kontakt</a>
  </nav>
</header>

<section class="hero">
  <div class="hero-panel"></div>
  <div class="hero-photo" role="img" aria-label="Foto: Metallarbeiter beim Trennschleifen mit Funkenflug"></div>
  <h1>Verlässliche Qualität.<br>Maßgeschneiderte Lösungen.</h1>
  <p>Von der Beratung über Planung und Fertigung bis hin zu Montage und Wartung: Unsere qualifizierten Mitarbeiter und modern ausgestattete Fertigung garantieren höchste Qualität!</p>
  <a class="btn btn-yellow" href="#" style="left:123px;width:86px">Leistungen ansehen</a>
  <a class="btn btn-white" href="#" style="left:216px;width:86px">Referenzen ansehen</a>
</section>

<div class="photo" style="left:123px;top:359px;width:172px;height:132px;background:linear-gradient(135deg,#3f6fb0,#5d6670 55%,#2f3438)" role="img" aria-label="Foto: Mitarbeiter in Arbeitskleidung an der Werkbank"></div>
<div class="card" style="left:123px;top:491px;width:172px;height:151px">
  <span class="kicker" style="left:20px;top:17px">Leistungen</span>
  <h2 style="left:20px;top:33px">Präzision, die überzeugt</h2>
  <p style="left:20px;top:56px;width:128px;color:#555">Von Planung über Fertigung bis Montage — wir liefern Qualität, auf die Sie zählen können.</p>
  <a class="btn btn-yellow" href="#" style="left:20px;top:95px;width:66px">Mehr erfahren</a>
</div>

<div class="photo" style="left:303px;top:359px;width:180px;height:132px;background:linear-gradient(160deg,#e4e2de,#a99a88 55%,#c6a47e)" role="img" aria-label="Foto: Treppe mit Stahlgeländer in hellem Treppenhaus"></div>
<div class="card" style="left:483px;top:359px;width:172px;height:132px">
  <span class="kicker" style="left:17px;top:15px">Referenzen</span>
  <h2 style="left:17px;top:29px">Erfahrung in jeder Lösung</h2>
  <p style="left:17px;top:51px;width:140px">Ein Blick auf erfolgreich abgeschlossene Projekte zeigt, wofür wir stehen: Kompetenz und Verlässlichkeit</p>
  <a class="btn btn-yellow" href="#" style="left:17px;top:91px;width:79px">Zu den Referenzen</a>
</div>

<div class="photo" style="left:303px;top:499px;width:180px;height:143px;background:linear-gradient(135deg,#6f6f6c,#9a948c 50%,#4a4a48)" role="img" aria-label="Foto: Lächelnder Arbeiter mit Schutzhelm in der Werkhalle"></div>
<div class="card" style="left:483px;top:499px;width:172px;height:143px">
  <span class="kicker" style="left:17px;top:14px">Stellenanzeigen</span>
  <h2 style="left:17px;top:28px;width:150px">Aktuelle Stellenausschreibungen</h2>
  <p style="left:17px;top:64px;width:122px">Werden Sie Teil unseres Teams und bringen Sie Ihre Ideen in sichere, hochwertige Projekte ein.</p>
  <a class="btn btn-yellow" href="#" style="left:17px;top:105px;width:68px">Jetzt bewerben</a>
</div>

<div class="divider"></div>

<div class="tile" style="left:121px">
  <div class="tile-icon"><span style="width:20px;height:20px;background:var(--yellow);display:block"></span></div>
  <h3>Das Unternehmen</h3>
  <p>Lorem ipsum dolor sit amet, consetetur sadipscing</p>
  <svg class="tile-arrow" width="10" height="8" viewBox="0 0 10 8"><path d="M0 4h9M6 1l3 3-3 3" fill="none" stroke="#06067a" stroke-width="1"/></svg>
</div>
<div class="tile" style="left:257px">
  <div class="tile-icon"><svg width="20" height="16" viewBox="0 0 20 16"><rect x="1" y="1" width="18" height="14" rx="1.5" fill="none" stroke="#f2cb6b" stroke-width="1.6"/><rect x="4" y="4" width="5" height="4" fill="none" stroke="#f2cb6b" stroke-width="1.3"/><path d="M11 5h5M11 8h5M4 11h12" stroke="#f2cb6b" stroke-width="1.3"/></svg></div>
  <h3>Aktuelle Meldungen</h3>
  <p>Lorem ipsum dolor sit amet, consetetur sadipscing</p>
  <svg class="tile-arrow" width="10" height="8" viewBox="0 0 10 8"><path d="M0 4h9M6 1l3 3-3 3" fill="none" stroke="#06067a" stroke-width="1"/></svg>
</div>
<div class="tile" style="left:391px">
  <div class="tile-icon"><svg width="18" height="18" viewBox="0 0 18 18"><path d="M9 2v9M5 7l4 4 4-4M2 12v3h14v-3" fill="none" stroke="#f2cb6b" stroke-width="1.7" stroke-linecap="round" stroke-linejoin="round"/></svg></div>
  <h3>Downloads</h3>
  <p>Lorem ipsum dolor sit amet, consetetur sadipscing</p>
  <svg class="tile-arrow" width="10" height="8" viewBox="0 0 10 8"><path d="M0 4h9M6 1l3 3-3 3" fill="none" stroke="#06067a" stroke-width="1"/></svg>
</div>
<div class="tile" style="left:526px">
  <div class="tile-icon"><svg width="20" height="20" viewBox="0 0 24 24"><path d="M5 3h4l2 5-2.5 1.5a11 11 0 0 0 6 6L16 13l5 2v4a2 2 0 0 1-2 2A16 16 0 0 1 3 5a2 2 0 0 1 2-2zM15 3a6 6 0 0 1 6 6M15 7a2 2 0 0 1 2 2" fill="none" stroke="#f2cb6b" stroke-width="1.8" stroke-linecap="round" stroke-linejoin="round"/></svg></div>
  <h3>Kontakt</h3>
  <p>Lorem ipsum dolor sit amet, consetetur sadipscing</p>
  <svg class="tile-arrow" width="10" height="8" viewBox="0 0 10 8"><path d="M0 4h9M6 1l3 3-3 3" fill="none" stroke="#06067a" stroke-width="1"/></svg>
</div>

<div class="contact-photo" role="img" aria-label="Foto: Glastür des Firmengebäudes mit Firmenbeschriftung, unscharfer Hintergrund mit Pflanzen"></div>
<section class="contact-panel">
  <h2>Wir sind für Sie da.</h2>
  <h4>Metall- und Stahlbau Harkenfeld GmbH</h4>
  <div class="info" style="top:99px">
    <svg width="8" height="9" viewBox="0 0 10 12"><path d="M5 11s4-4 4-6.5A4 4 0 0 0 1 4.5C1 7 5 11 5 11z" fill="none" stroke="#f2cb6b" stroke-width="1"/><circle cx="5" cy="4.5" r="1.4" fill="none" stroke="#f2cb6b"/></svg>
    <span>Lindenstraße 14<br>09471 Talberg</span>
  </div>
  <div class="info" style="top:133px">
    <svg width="8" height="20" viewBox="0 0 10 24"><path d="M2 1h2l1 2.5-1.2.8a5 5 0 0 0 3 3L7.6 6 10 7v2a1 1 0 0 1-1 1A8 8 0 0 1 1 2a1 1 0 0 1 1-1z" fill="none" stroke="#f2cb6b" stroke-width=".9"/><rect x="1" y="16" width="8" height="5" fill="none" stroke="#f2cb6b" stroke-width=".9"/><rect x="3" y="13" width="4" height="3" fill="none" stroke="#f2cb6b" stroke-width=".9"/></svg>
    <span>Tel.: 037312 4480<br>Fax: 037312 4481</span>
  </div>
  <div class="info" style="top:167px">
    <svg width="8" height="7" viewBox="0 0 10 8"><rect x=".5" y=".5" width="9" height="7" fill="none" stroke="#f2cb6b"/><path d="M.5 .5L5 4.5 9.5 .5" fill="none" stroke="#f2cb6b"/></svg>
    <span>info@stahlbau-harkenfeld.de</span>
  </div>
  <div class="info" style="top:190px">
    <svg width="8" height="8" viewBox="0 0 10 10"><circle cx="5" cy="5" r="4.4" fill="none" stroke="#f2cb6b" stroke-width=".9"/><ellipse cx="5" cy="5" rx="2" ry="4.4" fill="none" stroke="#f2cb6b" stroke-width=".9"/><path d="M.6 5h8.8" stroke="#f2cb6b" stroke-width=".9"/></svg>
    <span>Wir arbeiten bundesweit, in Österreich und der Schweiz.<br>Unsere Leistungen zum Strahlenschutzbau werden darüberhinaus auch in<br>Asien und auf dem afrikanischen Kontinent realisiert.</span>
  </div>
</section>

<footer class="site-footer">
  <span class="copyright">2026 © Metall- und Stahlbau Harkenfeld GmbH</span>
  <nav class="legal"><a href="#">Impressum</a><a href="#">Datenschutz</a><a href="#">Erklärung zur Barrierefreiheit</a></nav>
</footer>

</body>
</html>
```